Magazine Ad for TideGlen School of Music

This will be an ad for music lessons. Logo and text are included in sections below. It will be used for print in newspapers and magazines, so it must look good in black & white as well as in color.

We need an 8.5" x 11" magazine ad (full page), also a 8.5" x 5.5" ad (half page), a 4.25" x 5.5" ad (quarter page) and a business card size ad.

Target Market(s)

Active mothers with children

Industry/Entity Type

School

Font styles to use
Serif

Requirements
Must have
• Must use one of the company logos (see uploaded files).
• All these ads should include the following text:
• ______________
• Music lessons in the comfort of YOUR HOUSE with EXPERIENCED and professional staff.
• Piano, Guitar, voice, VIOLIN, Drums, songwriting, and others
• Email contact@tideglenmusic.example or call 555-417-3826
• www.TideGlenMusic.example
• ______________
• The ad must look stylish and sharp in both color and black & white.

```html
<!DOCTYPE html>
<html lang="en">
<head>
<meta charset="utf-8">
<title>TideGlen School of Music – Magazine Ad, Mono and Colour</title>
<link href="https://fonts.googleapis.com/css2?family=Archivo+Black&family=Josefin+Sans:wght@600;700&family=Roboto:wght@400&display=swap" rel="stylesheet">
<style>
  :root {
    --page-bg: #e9e6e1;
    --paper: #ffffff;
    --panel: #231f20;
    --ink-light: #ffffff;
    --divider: #4a4647;
    --ornament: #f0f0f0;
  }
  .ad--colour {
    --disc-inner: #2a0a1f;
    --disc-outer: #5c1745;
    --disc-edge: #7a2a63;
    --accent-1: #8cc63f;
    --accent-2: #f4d21d;
    --dot: #29b6e8;
    --bar-1: #f7d417; --bar-2: #f39223; --bar-3: #ec5a2b; --bar-4: #d8428f;
    --bar-5: #8e3b97; --bar-6: #29b6e8; --bar-7: #2e86c8; --bar-8: #8cc63f; --bar-9: #f7d417;
  }
  .ad--mono {
    --disc-inner: #1c1c1c;
    --disc-outer: #3a3a3a;
    --disc-edge: #6a6a6a;
    --accent-1: #b5b5b5;
    --accent-2: #a5a5a5;
    --dot: #a8a8a8;
    --bar-1: #7a7a7a; --bar-2: #9a9a9a; --bar-3: #6a6a6a; --bar-4: #8a8a8a;
    --bar-5: #5a5a5a; --bar-6: #9e9e9e; --bar-7: #777777; --bar-8: #8e8e8e; --bar-9: #7a7a7a;
  }
  * { box-sizing: border-box; margin: 0; padding: 0; }
  html, body { width: 1200px; height: 1200px; overflow: hidden; }
  body { background: var(--page-bg); position: relative; }

  .ad {
    position: absolute; top: 231px;
    width: 830px; height: 1070px;
    transform: scale(0.69); transform-origin: top left;
    background: var(--paper);
    overflow: hidden;
  }
  .ad--mono { left: 20px; }
  .ad--colour { left: 608px; }

  .ornament {
    position: absolute; top: 0; width: 120px; height: 300px;
    background: var(--ornament);
  }
  .ornament--left { left: 0; border-radius: 0 0 120px 0; }
  .ornament--right { right: 0; border-radius: 0 0 0 120px; }

  .social {
    position: absolute; top: 27px; left: 0; width: 100%;
    display: flex; justify-content: center; gap: 6px;
  }
  .social span { width: 36px; height: 36px; border-radius: 50%; background: var(--panel); }

  .illustration {
    position: absolute; left: 402px; top: 370px;
    width: 640px; height: 600px; margin: -300px 0 0 -320px;
    border-radius: 50%;
    background: radial-gradient(circle at 50% 50%,
      var(--disc-inner) 0 30%, var(--disc-outer) 58%, var(--disc-edge) 100%);
  }

  .brand {
    position: absolute; left: 402px; top: 395px; transform: translate(-50%, -50%);
    text-align: center; color: var(--ink-light);
    font-family: "Josefin Sans", sans-serif; font-weight: 600;
  }
  .brand__mark { width: 20px; height: 20px; border-radius: 50%; background: var(--ink-light); margin: 0 auto 18px; }
  .brand__name { font-size: 64px; line-height: 1; letter-spacing: -1px; }
  .brand__sub { font-size: 21px; margin-top: 8px; }

  .bar { position: absolute; left: 0; width: 100%; height: 14px; display: flex; }
  .bar span { flex: 1; }
  .bar span:nth-child(1) { background: var(--bar-1); }
  .bar span:nth-child(2) { background: var(--bar-2); }
  .bar span:nth-child(3) { background: var(--bar-3); }
  .bar span:nth-child(4) { background: var(--bar-4); }
  .bar span:nth-child(5) { background: var(--bar-5); }
  .bar span:nth-child(6) { background: var(--bar-6); }
  .bar span:nth-child(7) { background: var(--bar-7); }
  .bar span:nth-child(8) { background: var(--bar-8); }
  .bar span:nth-child(9) { background: var(--bar-9); }
  .bar--top { top: 677px; }
  .bar--bottom { top: 1056px; }

  .info {
    position: absolute; left: 0; top: 691px; width: 100%; height: 365px;
    background: var(--panel); color: var(--ink-light); text-align: center;
  }
  .info > * { position: absolute; left: 0; width: 100%; }
  .tagline {
    top: 21px;
    font-family: Roboto, sans-serif; font-size: 32px; line-height: 40px;
  }
  .tagline strong { font-family: "Archivo Black", sans-serif; font-weight: 400; letter-spacing: .5px; }
  .tagline .accent-1 { color: var(--accent-1); }
  .tagline .accent-2 { color: var(--accent-2); }

  .divider { top: 112px; left: 63px; width: 704px; height: 1px; background: var(--divider); }

  .lessons {
    top: 123px;
    font-family: "Josefin Sans", sans-serif; font-weight: 700;
    font-size: 31px; line-height: 38px;
  }
  .lessons .dot {
    display: inline-block; width: 12px; height: 12px; border-radius: 50%;
    background: var(--dot); margin: 0 14px; vertical-align: 5px;
  }

  .phone {
    top: 222px;
    display: flex; justify-content: center; align-items: center; gap: 10px;
    font-family: "Archivo Black", sans-serif; font-size: 56px; line-height: 1;
    letter-spacing: 1px;
  }
  .phone svg { width: 36px; height: 50px; }

  .contacts {
    top: 303px;
    display: flex; justify-content: center; gap: 44px;
    font-family: Roboto, sans-serif; font-size: 20px; letter-spacing: 1px;
  }
  .contacts span { display: flex; align-items: center; gap: 8px; }
  .contacts svg { width: 32px; height: 24px; }
</style>
</head>
<body>
  <main class="ad ad--mono">
    <div class="ornament ornament--left" role="img" aria-label="Swirl of music staff lines and notes"></div>
    <div class="ornament ornament--right" role="img" aria-label="Swirl of music staff lines and notes"></div>
    <div class="social" aria-label="Social media links"><span></span><span></span><span></span><span></span></div>
    <div class="illustration" role="img" aria-label="Black and grey ring of musical instrument silhouettes around a dark circle"></div>
    <div class="brand">
      <div class="brand__mark"></div>
      <div class="brand__name">TideGlen</div>
      <div class="brand__sub">School of Music</div>
    </div>
    <div class="bar bar--top"><span></span><span></span><span></span><span></span><span></span><span></span><span></span><span></span><span></span></div>
    <section class="info">
      <p class="tagline">Music lessons in the comfort of <strong class="accent-1">YOUR HOUSE</strong><br>with <strong class="accent-2">EXPERIENCED</strong> and professional staff.</p>
      <div class="divider"></div>
      <p class="lessons">Piano<span class="dot"></span>Guitar<span class="dot"></span>Voice<span class="dot"></span>Violin<span class="dot"></span>Drums<br>Songwriting&nbsp; And Others</p>
      <p class="phone"><svg viewBox="0 0 40 56" aria-hidden="true"><path d="M10 4 L16 4 L19 16 L14 19 C15 28 19 36 25 41 L29 37 L37 44 L33 52 C20 52 6 34 6 16 Z" fill="none" stroke="#fff" stroke-width="4" stroke-linejoin="round"/></svg>555-417-3826</p>
      <div class="contacts">
        <span><svg viewBox="0 0 36 26" aria-hidden="true"><rect x="1.5" y="1.5" width="33" height="23" fill="none" stroke="#fff" stroke-width="3"/><path d="M2 2 L18 15 L34 2 M2 24 L14 12 M34 24 L22 12" fill="none" stroke="#fff" stroke-width="3"/></svg>contact@tideglenmusic.example</span>
        <span><svg viewBox="0 0 36 26" aria-hidden="true"><circle cx="18" cy="13" r="11" fill="none" stroke="#fff" stroke-width="2"/><ellipse cx="18" cy="13" rx="5" ry="11" fill="none" stroke="#fff" stroke-width="2"/><path d="M7 13 H29 M9 7 H27 M9 19 H27" stroke="#fff" stroke-width="2"/></svg>www.TideGlenMusic.example</span>
      </div>
    </section>
    <div class="bar bar--bottom"><span></span><span></span><span></span><span></span><span></span><span></span><span></span><span></span><span></span></div>
  </main>

  <main class="ad ad--colour">
    <div class="ornament ornament--left" role="img" aria-label="Swirl of music staff lines and notes"></div>
    <div class="ornament ornament--right" role="img" aria-label="Swirl of music staff lines and notes"></div>
    <div class="social" aria-label="Social media links"><span></span><span></span><span></span><span></span></div>
    <div class="illustration" role="img" aria-label="Colourful ring of musical instrument silhouettes around a dark plum circle"></div>
    <div class="brand">
      <div class="brand__mark"></div>
      <div class="brand__name">TideGlen</div>
      <div class="brand__sub">School of Music</div>
    </div>
    <div class="bar bar--top"><span></span><span></span><span></span><span></span><span></span><span></span><span></span><span></span><span></span></div>
    <section class="info">
      <p class="tagline">Music lessons in the comfort of <strong class="accent-1">YOUR HOUSE</strong><br>with <strong class="accent-2">EXPERIENCED</strong> and professional staff.</p>
      <div class="divider"></div>
      <p class="lessons">Piano<span class="dot"></span>Guitar<span class="dot"></span>Voice<span class="dot"></span>Violin<span class="dot"></span>Drums<br>Songwriting&nbsp; And Others</p>
      <p class="phone"><svg viewBox="0 0 40 56" aria-hidden="true"><path d="M10 4 L16 4 L19 16 L14 19 C15 28 19 36 25 41 L29 37 L37 44 L33 52 C20 52 6 34 6 16 Z" fill="none" stroke="#fff" stroke-width="4" stroke-linejoin="round"/></svg>555-417-3826</p>
      <div class="contacts">
        <span><svg viewBox="0 0 36 26" aria-hidden="true"><rect x="1.5" y="1.5" width="33" height="23" fill="none" stroke="#fff" stroke-width="3"/><path d="M2 2 L18 15 L34 2 M2 24 L14 12 M34 24 L22 12" fill="none" stroke="#fff" stroke-width="3"/></svg>contact@tideglenmusic.example</span>
        <span><svg viewBox="0 0 36 26" aria-hidden="true"><circle cx="18" cy="13" r="11" fill="none" stroke="#fff" stroke-width="2"/><ellipse cx="18" cy="13" rx="5" ry="11" fill="none" stroke="#fff" stroke-width="2"/><path d="M7 13 H29 M9 7 H27 M9 19 H27" stroke="#fff" stroke-width="2"/></svg>www.TideGlenMusic.example</span>
      </div>
    </section>
    <div class="bar bar--bottom"><span></span><span></span><span></span><span></span><span></span><span></span><span></span><span></span><span></span></div>
  </main>
</body>
</html>
```